Velmonta ice cream tub packaging

We need new tub designs for our dairy free ice cream. It is made with avocado and coconut which we would like communicated within the design. We launched last year and have had positive feedback regarding our current packaging but also that it could be a cleaner design with a more sophisticated font as it will be sold in more high end expensive stores. I have attached our current packaging for info (there are 3 flavours - Original Avocado, Raspberry and Basil, Raw Cacao) We would like to keep the avocado print that is currently included on the packaging as we have had a lot of very positive feedback about that. Maybe not as much though as it makes it quite busy and we prefer a clean design.
I've also attached our new logo.
We would like it to mention we are gluten, soya, dairy, egg and nut free. And that it is a 'coconut and avocado ice cream' rather than an 'alternative'.
The nutritional label needs to be in a UK table format (I've attached a blank copy for information). We don't currently have the values for the table as it has been sent off for testing as we have a new recipe. But if you could leave that blank we will fill it in when we have the results.
I've attached the template for the sizes as we have two sizes - 500ml and 100ml. The designs will be the same but just smaller/bigger. It has to be font size 11 for legal purpose.
It has to have the weight (100ml and 500ml) followed by the official e-mark.
The ingredients are the same but take out Locust Bean Gum and replace Vanilla extract with Lime Juice.
The business address is the same but should read 'Velmonta LTD'. All other info on the packaging (barcode, text etc) is to remain the same.
I've have also attached 3 pictures of other tub designs that we like for inspiration - our favourite is 'lusk' as we can have half the print half the colour if the flavour (raspberry/pink, cacao/brown, original/green)
Updates
Target Market(s)
High end health food stores
Look and feel

```html
<!DOCTYPE html>
<html lang="en">
<head>
<meta charset="utf-8">
<title>Velmonta ice cream tub packaging</title>
<link rel="stylesheet" href="https://fonts.googleapis.com/css2?family=Ubuntu:wght@300;400&family=PT+Serif:wght@400;700&display=swap">
<style>
  :root {
    --backdrop: #e9e9e9;
    --cacao: #773a12;
    --leaf: #ccff99;
    --leaf-pale: #f1fbc4;
    --avocado: #5f8a2f;
    --ink: #1a1a1a;
    --paper: #ffffff;
    --label-brown: #5a2a0c;
    --label-green: #3e5a1c;
  }
  html, body {
    margin: 0;
    padding: 0;
    width: 1200px;
    height: 1200px;
    overflow: hidden;
  }
  body {
    background: radial-gradient(circle at 50% 45%, #fafafa 0%, var(--backdrop) 75%);
    position: relative;
    font-family: "Ubuntu", sans-serif;
  }
  .artwork {
    position: absolute;
    inset: 0;
    width: 1200px;
    height: 1200px;
  }
  .lid, .sleeve-shape {
    filter: drop-shadow(0 10px 18px rgba(0,0,0,0.18));
  }
  .seal-text {
    font-family: "Ubuntu", sans-serif;
    font-weight: 400;
    font-size: 21px;
    fill: var(--label-brown);
  }
  .seal-text--top { fill: var(--label-green); font-size: 22px; }
  .brand-name {
    font-family: "Ubuntu", sans-serif;
    font-weight: 400;
    font-size: 44px;
    letter-spacing: 1px;
    fill: var(--avocado);
  }

  .nutrition-label {
    position: absolute;
    left: 244px;
    top: 768px;
    width: 196px;
    padding: 8px 9px 10px;
    background: var(--paper);
    border: 1px solid #999;
    transform: rotate(-14deg);
    transform-origin: center;
    font-family: "PT Serif", serif;
    font-size: 7px;
    line-height: 1.15;
    color: var(--ink);
  }
  .nutrition-label h3 {
    margin: 0 0 2px;
    font-size: 8px;
    font-weight: 700;
    border-bottom: 1px solid var(--ink);
    padding-bottom: 1px;
  }
  .nutrition-label table {
    width: 100%;
    border-collapse: collapse;
  }
  .nutrition-label th {
    font-weight: 400;
    text-align: left;
    vertical-align: bottom;
    border-bottom: 1px solid var(--ink);
    padding: 0 2px 1px 0;
  }
  .nutrition-label td {
    padding: 0 2px 0 0;
    vertical-align: top;
  }
  .nutrition-label .num { text-align: right; }
  .nutrition-label .sub { padding-left: 4px; }
  .nutrition-label .footer-row td {
    border-top: 1px solid var(--ink);
    padding-top: 2px;
  }
  .nutrition-label .note {
    margin: 5px 0 0;
  }

  .ingredients-panel {
    position: absolute;
    left: 800px;
    top: 736px;
    width: 180px;
    padding: 6px 4px;
    background: rgba(255,255,255,0.55);
    transform: rotate(15deg);
    transform-origin: center;
    font-family: "PT Serif", serif;
    font-size: 9.6px;
    line-height: 1.18;
    text-align: center;
    color: var(--ink);
  }
  .ingredients-panel p { margin: 0 0 6px; }
  .ingredients-panel .heading { margin-bottom: 1px; }

  .maker-name {
    position: absolute;
    left: 802px;
    top: 942px;
    width: 100px;
    transform: rotate(15deg);
    font-family: "PT Serif", serif;
    font-size: 11px;
    font-weight: 700;
    color: var(--ink);
    text-align: center;
  }

  .flavour-tag {
    position: absolute;
    left: 554px;
    top: 964px;
    width: 81px;
    height: 22px;
    background: var(--cacao);
    color: var(--paper);
    font-family: "PT Serif", serif;
    font-weight: 700;
    font-size: 10px;
    line-height: 22px;
    text-align: center;
  }
  .volume-mark {
    position: absolute;
    left: 566px;
    top: 988px;
    font-family: "PT Serif", serif;
    font-weight: 700;
    font-size: 11px;
    color: var(--ink);
  }
</style>
</head>
<body>

<svg class="artwork" viewBox="0 0 1200 1200" xmlns="http://www.w3.org/2000/svg">
  <defs>
    <path id="arc-top" d="M -131.4 -61.3 A 145 145 0 0 1 131.4 -61.3"/>
    <path id="arc-bottom" d="M -166.1 -44.5 A 172 172 0 1 0 166.1 -44.5"/>
    <clipPath id="sleeve-clip">
      <path d="M 168 728 Q 600 620 1036 730 L 948 1060 Q 600 990 248 1060 Z"/>
    </clipPath>

    <g id="seal">
      <circle class="avocado-print" r="240" fill="var(--leaf)" role="img" aria-label="Repeating avocado half print in light green"/>
      <circle r="181" fill="var(--paper)"/>
      <text class="seal-text seal-text--top">
        <textPath href="#arc-top" startOffset="0" textLength="322" lengthAdjust="spacing">•coconut and avocado ice cream•</textPath>
      </text>
      <text class="seal-text">
        <textPath href="#arc-bottom" startOffset="0" textLength="615" lengthAdjust="spacing">vegan • dairy free • gluten free • refined sugaer free• frozen desert</textPath>
      </text>
      <text class="brand-name" x="0" y="15" text-anchor="middle">VELMONTA</text>
    </g>
  </defs>

  <g class="lid">
    <circle cx="600" cy="328" r="302" fill="var(--cacao)"/>
    <use href="#seal" transform="translate(600 328)"/>
  </g>

  <g class="sleeve">
    <path class="sleeve-shape" d="M 168 728 Q 600 620 1036 730 L 948 1060 Q 600 990 248 1060 Z" fill="var(--leaf-pale)"/>
    <g clip-path="url(#sleeve-clip)">
      <rect class="avocado-print" x="480" y="640" width="580" height="440" fill="var(--leaf-pale)" role="img" aria-label="Repeating avocado half print on pale green"/>
      <polygon class="cacao-band" points="150,620 800,620 792,686 704,784 596,836 560,940 480,1024 150,1100" fill="var(--cacao)"/>
      <circle cx="596" cy="836" r="116" fill="var(--cacao)"/>
    </g>
    <use href="#seal" transform="translate(596 836) scale(0.383)"/>
  </g>
</svg>

<div class="nutrition-label">
  <h3>Nutrition</h3>
  <table>
    <tr>
      <th>Typical values</th>
      <th>100ml contains</th>
      <th>% RI*</th>
      <th class="num">RI* for an average adult</th>
    </tr>
    <tr><td>Energy</td><td>kJ<br>kcal</td><td>%<br>%</td><td class="num">8400kJ<br>2000kcal</td></tr>
    <tr><td>Fat</td><td>g</td><td>%</td><td class="num">70g</td></tr>
    <tr><td class="sub">of which saturates</td><td>g</td><td>%</td><td class="num">20g</td></tr>
    <tr><td>Carbohydrate</td><td>g</td><td>%</td><td class="num">260g</td></tr>
    <tr><td class="sub">of which sugars</td><td>g</td><td>%</td><td class="num">90g</td></tr>
    <tr><td>Fibre</td><td>g</td><td></td><td class="num"></td></tr>
    <tr><td>Protein</td><td>g</td><td>%</td><td class="num">50g</td></tr>
    <tr><td>Salt</td><td>g</td><td>%</td><td class="num">6g</td></tr>
    <tr class="footer-row"><td colspan="2">This pack contains</td><td colspan="2">servings</td></tr>
  </table>
  <p class="note">*Reference intake of an average adult (8400kJ / 2000kcal)</p>
</div>

<div class="ingredients-panel">
  <p class="heading">INGRIDIENTS:</p>
  <p>Coconut milk, Avocados, Organic light agave syrup, Coconut oil, Cacao, Lime juice, Arrowroot, Guar gum, Xanthan gum, Salt.</p>
  <p>Made from coconut flesh and creamy avocado with a swirl of raw cacao fudge sauce this ice cream offers an indulgent dairy -free treat.</p>
  <p>For Best Before see base. Storage conditions - keep frozen -18 o C. Best removed from freezer 5 minutes before serving.</p>
</div>

<div class="maker-name">Velmonta LTD</div>

<div class="flavour-tag">Raw Cacao</div>
<div class="volume-mark">500 ml ℮</div>

</body>
</html>
```